Visitenkarten
Zielgruppe
Wir handeln und restaurieren (mit) sehr hochwertigen Fahrzeugen (Oldtimier/Supercars) bis in den Bereich von mehreren Millionen Euro. Die Zielgruppe sind potentielle Käufer im sehr gehobenen Premium Segment.
Aufgabenstellung
Eine Visitenkarte im Idealfall mit dem schwarzen Logo soll erstellt werden. Standardformat oder ein kreatives, aber praktikables Format. Ziel ist eine sehr hochwertige, geprägte Visitenkarte. Frontseite das Velvet Marques Logo, Rückseite einmal: Jonas Wehrberg, Owner, Phone +436601742863, Email Sales@velvet-marques.com Salzburg Dobrovnik (generisch anpassbare Adresse)

```html
<!DOCTYPE html>
<html lang="de">
<head>
<meta charset="utf-8">
<title>Velvet Marques – Visitenkarten</title>
<link rel="stylesheet" href="https://fonts.googleapis.com/css2?family=Jost:wght@300;400&display=swap">
<style>
  :root {
    --stage: #67656b;
    --card-white: #ffffff;
    --ink: #111111;
    --ink-soft: #2a2a2a;
    --gold-light: #ecc9a0;
    --gold-mid: #d2a77c;
    --gold-deep: #b78960;
    --bronze-dark: #5a4128;
    --bronze-shine: #f1cfa6;
  }
  * { margin: 0; padding: 0; box-sizing: border-box; }
  html, body {
    width: 1200px;
    height: 675px;
    overflow: hidden;
    background: var(--stage);
  }
  .stage {
    position: relative;
    width: 1200px;
    height: 675px;
  }
  .card {
    position: absolute;
    top: 200px;
    width: 419px;
    height: 275px;
    display: flex;
    background: var(--card-white);
    box-shadow: 2px 3px 6px rgba(0,0,0,0.35);
  }
  .card--front { left: 146px; }
  .card--back  { left: 636px; }

  .pattern-band {
    width: 75px;
    height: 100%;
    flex: none;
    background: linear-gradient(90deg, var(--gold-mid) 0%, var(--gold-light) 30%, var(--gold-deep) 70%, var(--gold-mid) 100%);
  }
  .metal-stripe {
    width: 9px;
    height: 100%;
    flex: none;
    background: linear-gradient(180deg, var(--bronze-dark) 0%, var(--gold-deep) 30%, var(--bronze-dark) 55%, var(--bronze-shine) 85%, var(--gold-deep) 100%);
  }
  .card-face {
    flex: 1;
    position: relative;
    text-align: center;
    font-family: "Jost", sans-serif;
    color: var(--ink);
    white-space: nowrap;
  }

  .brand-wordmark {
    position: absolute;
    left: 0; right: 0;
    top: 148px;
    font-weight: 400;
    font-size: 22px;
    line-height: 1;
    letter-spacing: 0.07em;
    text-transform: uppercase;
    color: var(--ink);
  }

  .brand-mark {
    position: absolute;
    left: 0; right: 0;
    top: 58px;
    font-weight: 400;
    font-size: 14px;
    line-height: 1;
    letter-spacing: 0.18em;
    text-transform: uppercase;
    color: var(--ink);
  }
  .contact-name {
    position: absolute;
    left: 0; right: 0;
    top: 112px;
    font-weight: 400;
    font-size: 19px;
    line-height: 1.2;
    letter-spacing: 0.09em;
  }
  .contact-role {
    position: absolute;
    left: 0; right: 0;
    top: 137px;
    font-weight: 300;
    font-size: 14px;
    line-height: 1.2;
    letter-spacing: 0.08em;
    color: var(--ink-soft);
  }
  .contact-line {
    position: absolute;
    left: 0; right: 0;
    font-weight: 400;
    font-size: 12px;
    line-height: 1.2;
    letter-spacing: 0.1em;
    color: var(--ink-soft);
  }
  .contact-line--city  { top: 174px; }
  .contact-line--email { top: 201px; }
  .contact-line--phone { top: 227px; }
</style>
</head>
<body>
<main class="stage">

  <section class="card card--front" aria-label="Vorderseite">
    <div class="pattern-band" role="img" aria-label="Goldenes Rautenmuster mit schwarzen Sternpunkten"></div>
    <div class="metal-stripe"></div>
    <div class="card-face">
      <div class="brand-wordmark">Velvet Marques</div>
    </div>
    <div class="metal-stripe"></div>
    <div class="pattern-band" role="img" aria-label="Goldenes Rautenmuster mit schwarzen Sternpunkten"></div>
  </section>

  <section class="card card--back" aria-label="Rückseite">
    <div class="pattern-band" role="img" aria-label="Goldenes Rautenmuster mit schwarzen Sternpunkten"></div>
    <div class="metal-stripe"></div>
    <div class="card-face">
      <div class="brand-mark">Velvet Marques</div>
      <div class="contact-name">Jonas Wehrberg</div>
      <div class="contact-role">Owner</div>
      <div class="contact-line contact-line--city">Innsbruck / Rovinj</div>
      <div class="contact-line contact-line--email">sales@velvet-marques.com</div>
      <div class="contact-line contact-line--phone">+43 66 01 74 28 63</div>
    </div>
    <div class="metal-stripe"></div>
    <div class="pattern-band" role="img" aria-label="Goldenes Rautenmuster mit schwarzen Sternpunkten"></div>
  </section>

</main>
</body>
</html>
```